Business Card Design

I give lessons and clinics for dressage riders
I would like the design to be an outline (with broad lines) of a dressage horse and rider with in background of whole card with print over top tan or parchment card with burgundy print

Industry/Entity Type

Business

Contact Information for Business Card

Tod Harlick
555-317-0492
Classical dressage training for the modern American
Clinics, lessons, training level -Prix St. George

Requirements
Must have
• broad lined outline of dressage horse and rider

```html
<!DOCTYPE html>
<html lang="en">
<head>
<meta charset="utf-8">
<title>Tod Harlick — Business Card</title>
<link href="https://fonts.googleapis.com/css2?family=Arimo:wght@400&display=swap" rel="stylesheet">
<style>
  :root {
    --page-bg: #e9e6e1;
    --card-bg: #ffffff;
    --ink: #3f3f3f;
    --ink-soft: #555555;
    --art-light: #d6d6d6;
    --art-mid: #b3b3b3;
  }
  * { margin: 0; padding: 0; box-sizing: border-box; }
  html, body {
    width: 1200px;
    height: 800px;
    overflow: hidden;
    background: var(--page-bg);
    font-family: "Arimo", Arial, sans-serif;
  }
  .card {
    position: absolute;
    left: 75px;
    top: 100px;
    width: 1050px;
    height: 600px;
    background: var(--card-bg);
    overflow: hidden;
    box-shadow: 0 6px 24px rgba(0,0,0,0.12);
  }
  .rider-art {
    position: absolute;
    left: 0;
    top: 40px;
    width: 540px;
    height: 560px;
    background: radial-gradient(ellipse at 60% 55%, var(--art-mid) 0%, var(--art-light) 55%, var(--card-bg) 100%);
  }
  .details {
    position: absolute;
    left: 610px;
    top: 215px;
    color: var(--ink);
  }
  .name {
    font-size: 36px;
    font-weight: 400;
    letter-spacing: 0.5px;
    line-height: 1.1;
  }
  .phone {
    display: flex;
    align-items: center;
    gap: 8px;
    font-size: 22px;
    color: var(--ink-soft);
    margin-top: 4px;
  }
  .phone svg { width: 16px; height: 16px; fill: var(--ink); }
  .services {
    list-style: none;
    margin-top: 26px;
    font-size: 22px;
    line-height: 1.25;
    color: var(--ink-soft);
  }
  .services li { margin-bottom: 10px; }
  .tagline { max-width: 380px; }
</style>
</head>
<body>
  <div class="card">
    <div class="rider-art" role="img" aria-label="Broad-lined grey outline illustration of a dressage horse and rider"></div>
    <div class="details">
      <h1 class="name">Tod Harlick</h1>
      <div class="phone">
        <svg viewBox="0 0 24 24" aria-hidden="true"><path d="M6.6 10.8a15.1 15.1 0 0 0 6.6 6.6l2.2-2.2a1 1 0 0 1 1-.25 11.4 11.4 0 0 0 3.6.57 1 1 0 0 1 1 1V20a1 1 0 0 1-1 1A17 17 0 0 1 3 4a1 1 0 0 1 1-1h3.5a1 1 0 0 1 1 1c0 1.25.2 2.45.57 3.57a1 1 0 0 1-.25 1z"/></svg>
        <span>555-317-0492</span>
      </div>
      <ul class="services">
        <li class="tagline">Classical dressage training for the modern American Clinics</li>
        <li>lessons</li>
        <li>training level</li>
        <li>Prix St. George</li>
      </ul>
    </div>
  </div>
</body>
</html>
```